Design for Cedar Lark Homes real estate agency

Incorporate logo into new business cards. I need to include the Brindley Vance logo incorporated into Cedar Lark Homes on one side of the card (attached). On the other side I see just the icon with "Maren Quill" (attached) with "Guided with Candor" either included as is or removed from logo and rather put as a tag line on the business card separate from the main logo. Contact information:

Maren Quill
Associate Broker
Cell: 730-418-5093
Email: marenquill@cedarlarkhomes.example
Web: www.cedarlarkhomes.example

Target Market(s)

Buyers, Sellers, Builders and Investors of homes and land

Industry/Entity Type

Real Estate Agent

Contact Information for Business Card

My client base tend to be higher end home buyers, sellers, builders and investors. I have been more and more in land and subdivisions for builders and investors. The card should not be cluttered. Clean and simple - yet with an air of exclusive/high end

Colors

Designer to choose colors to be used in the design.

Requirements
Must have
• Must have the logo on one side that has Brindley Vance logo incorporated. The side that has my contact information does not have to have the Brindley Vance logo incorporated.
• Must include "Guided with Candor" tag line either within logo (as is) or removed from logo and included in another position on the side of the business card with contact information.
Should not have
• Should not have Brindley Vance logo incorporated into Cedar Lark Homes logo on both sides of business card. Would like the Cedar Lark Homes logo that has Brindley Logo only on the back side of card without contact information.

```html
<!DOCTYPE html>
<html lang="en">
<head>
<meta charset="utf-8">
<title>Maren Quill — Business Card</title>
<link href="https://fonts.googleapis.com/css2?family=Cinzel:wght@500;600&family=Roboto:wght@400&family=Roboto+Condensed:wght@500&display=swap" rel="stylesheet">
<style>
  :root {
    --backdrop: #e6e6e6;
    --paper: #f3f3f1;
    --umber: #5a3b08;
    --gold: #c6a823;
    --gold-card: #c8a724;
    --white: #ffffff;
  }
  * { margin: 0; padding: 0; box-sizing: border-box; }
  html, body { width: 1200px; height: 960px; overflow: hidden; }
  body { background: var(--backdrop); position: relative; }

  .card {
    position: absolute;
    width: 600px;
    height: 344px;
    border-radius: 22px;
    overflow: hidden;
  }
  .card--front { left: 314px; top: 113px; background: var(--paper); }
  .card--back  { left: 311px; top: 472px; background: var(--gold-card); }

  .card__wave { position: absolute; inset: 0; width: 600px; height: 344px; }

  /* Front brand block */
  .brand-front {
    position: absolute;
    left: 303px; top: 34px; width: 216px;
    text-align: center;
  }
  .brand-front__dot {
    width: 76px; height: 76px; border-radius: 50%;
    background: var(--gold);
    margin: 0 auto 32px;
  }
  .brand-front__name {
    font-family: "Cinzel", serif;
    font-weight: 500;
    font-size: 24px;
    letter-spacing: 2px;
    color: var(--umber);
    line-height: 1;
  }
  .brand-front__tagline {
    font-family: "Roboto", sans-serif;
    font-size: 7px;
    letter-spacing: 2.4px;
    color: var(--umber);
    margin-top: 4px;
  }

  /* Contact list */
  .contact {
    position: absolute;
    left: 40px; top: 262px;
    list-style: none;
    font-family: "Roboto", sans-serif;
    font-size: 14px;
    color: var(--white);
  }
  .contact li { display: flex; align-items: center; height: 19.5px; }
  .contact svg { width: 14px; height: 14px; margin-right: 8px; fill: var(--gold); }

  .agent {
    position: absolute;
    right: 46px; top: 275px;
    text-align: right;
  }
  .agent__name {
    font-family: "Roboto Condensed", sans-serif;
    font-weight: 500;
    font-size: 21px;
    color: var(--gold);
    line-height: 1.1;
  }
  .agent__title {
    font-family: "Roboto", sans-serif;
    font-weight: 400;
    font-size: 15px;
    color: var(--white);
    letter-spacing: 0.4px;
    margin-top: 3px;
  }

  /* Back lockup */
  .lockup {
    position: absolute;
    left: 106px; top: 116px;
    display: flex; align-items: center;
  }
  .lockup__dot {
    width: 86px; height: 86px; border-radius: 50%;
    background: var(--umber);
    margin-right: 13px;
  }
  .lockup__text { width: 280px; }
  .lockup__name {
    font-family: "Cinzel", serif;
    font-weight: 600;
    font-size: 28px;
    color: var(--umber);
    line-height: 1;
    white-space: nowrap;
  }
  .lockup__row {
    display: flex; align-items: center;
    margin-top: 6px;
  }
  .lockup__rule { flex: 1; height: 1px; background: var(--umber); }
  .lockup__agent {
    font-family: "Cinzel", serif;
    font-size: 13px;
    letter-spacing: 2px;
    color: var(--umber);
    padding: 0 8px;
    line-height: 1;
  }
  .lockup__partner {
    font-family: "Roboto Condensed", sans-serif;
    font-weight: 500;
    font-size: 10px;
    color: var(--umber);
    white-space: nowrap;
    padding-left: 4px;
  }
  .lockup__tagline {
    font-family: "Roboto", sans-serif;
    font-size: 6.5px;
    letter-spacing: 2.4px;
    color: var(--umber);
    text-align: center;
    margin-top: 2px;
    padding-right: 64px;
  }
  .back-url {
    position: absolute;
    left: 0; right: 0; top: 286px;
    text-align: center;
    font-family: "Roboto", sans-serif;
    font-size: 14px;
    letter-spacing: 3px;
    color: var(--umber);
  }
</style>
</head>
<body>

<section class="card card--front" aria-label="Card front with contact details">
  <svg class="card__wave" viewBox="0 0 600 344" aria-hidden="true">
    <path fill="var(--gold)" d="M0,188 C70,150 150,140 230,168 C270,182 300,200 320,212 C250,194 150,176 0,200 Z"/>
    <path fill="var(--gold)" d="M296,202 C360,222 420,240 470,236 C530,230 570,190 590,142 C580,196 540,244 480,248 C420,252 360,232 296,202 Z"/>
    <path fill="var(--umber)" d="M0,200 C90,172 200,186 300,212 C360,228 420,254 482,252 C548,248 585,200 600,136 L600,344 L0,344 Z"/>
    <path fill="none" stroke="var(--white)" stroke-width="2" d="M0,200 C90,172 200,186 300,212 C360,228 420,254 482,252 C548,248 585,200 600,136"/>
  </svg>

  <div class="brand-front">
    <div class="brand-front__dot"></div>
    <div class="brand-front__name">Maren Quill</div>
    <div class="brand-front__tagline">GUIDED WITH CANDOR</div>
  </div>

  <ul class="contact">
    <li><svg viewBox="0 0 14 14"><path d="M4,0 h6 a1,1 0 0 1 1,1 v12 a1,1 0 0 1 -1,1 h-6 a1,1 0 0 1 -1,-1 v-12 a1,1 0 0 1 1,-1 Z M4.5,1.5 v9.5 h5 v-9.5 Z"/></svg>730-418-5093</li>
    <li><svg viewBox="0 0 14 14"><path d="M1,3 h12 v8 h-12 Z M1.5,3.5 l5.5,4 l5.5,-4" stroke="var(--umber)" stroke-width="1"/></svg>marenquill@cedarlarkhomes.example</li>
    <li><svg viewBox="0 0 14 14"><circle cx="7" cy="7" r="6"/><path d="M3,5 h8 M3,9 h8 M7,1 v12" stroke="var(--umber)" stroke-width="0.9"/></svg>www.cedarlarkhomes.example</li>
  </ul>

  <div class="agent">
    <div class="agent__name">MAREN QUILL</div>
    <div class="agent__title">ASSOCIATE BROKER</div>
  </div>
</section>

<section class="card card--back" aria-label="Card back with brand lockup">
  <div class="lockup">
    <div class="lockup__dot"></div>
    <div class="lockup__text">
      <div class="lockup__name">Cedar Lark Homes</div>
      <div class="lockup__row">
        <span class="lockup__rule"></span>
        <span class="lockup__agent">MAREN QUILL</span>
        <span class="lockup__rule"></span>
        <span class="lockup__partner">Brindley Vance</span>
      </div>
      <div class="lockup__tagline">GUIDED WITH CANDOR</div>
    </div>
  </div>
  <div class="back-url">www.cedarlarkhomes.example</div>
</section>

</body>
</html>
```